Security Business card

I need a new business card for my new company Bastion Crest Security Group we provide security for clubs,pubs,hotels etc. I would like to see the main colors red and black to be used. The final design should communicate honor and integrity.

Industry/Entity Type

Security

Contact Information for Business Card

Marcus Delvane
Company Name-Bastion Crest Security Group
Abn-47318265094
Acn-318265094
address- po box 7352 Ferndale nsw 2291
phone- 0437682915
email- Marcus@bastioncrest.com.au

```html
<!DOCTYPE html>
<html lang="en">
<head>
<meta charset="utf-8">
<title>Bastion Crest Security Group – Business Card</title>
<link rel="stylesheet" href="https://fonts.googleapis.com/css2?family=Archivo+Black&family=Arimo:wght@400&display=swap">
<style>
  :root {
    --card-red: #ff0a00;
    --ink: #111111;
    --paper: #ffffff;
    --backdrop: #e6e6e6;
    --head-font: "Archivo Black", "Arial Black", sans-serif;
    --body-font: "Arimo", Arial, sans-serif;
  }
  * { margin: 0; padding: 0; box-sizing: border-box; }
  html, body {
    width: 1200px;
    height: 1000px;
    overflow: hidden;
    background: var(--backdrop);
  }
  .card {
    position: absolute;
    left: 47px;
    top: 160px;
    width: 1106px;
    height: 680px;
    background: var(--card-red);
    overflow: hidden;
  }
  .company-band {
    position: absolute;
    left: 0;
    top: 510px;
    width: 100%;
    height: 75px;
    background: var(--paper);
  }
  .shield {
    position: absolute;
    left: 0;
    top: 0;
    width: 360px;
    height: 680px;
  }
  .brand-name {
    position: absolute;
    left: 40px;
    top: 216px;
    width: 240px;
    text-align: center;
    font-family: var(--head-font);
    font-size: 30px;
    line-height: 1.1;
    color: var(--ink);
  }
  .holder-name {
    position: absolute;
    right: 68px;
    top: 232px;
    font-family: var(--head-font);
    font-size: 46px;
    letter-spacing: 1px;
    color: var(--ink);
  }
  .contact {
    position: absolute;
    right: 68px;
    top: 314px;
    text-align: right;
    font-family: var(--body-font);
    font-size: 29px;
    line-height: 37px;
    color: var(--ink);
    font-style: normal;
  }
  .company-name {
    position: absolute;
    left: 66px;
    right: 68px;
    top: 512px;
    text-align: right;
    font-family: var(--head-font);
    font-size: 55px;
    line-height: 72px;
    letter-spacing: 1px;
    color: var(--ink);
    white-space: nowrap;
  }
  .registration {
    position: absolute;
    right: 68px;
    top: 592px;
    font-family: var(--body-font);
    font-size: 28px;
    color: var(--ink);
  }
</style>
</head>
<body>
  <section class="card">
    <div class="company-band"></div>

    <svg class="shield" viewBox="0 0 360 680" aria-hidden="true">
      <path fill="var(--ink)" d="M0,0 C110,44 230,50 338,52 C346,53 348,58 348,66 C350,250 328,430 190,600 C140,650 70,676 22,680 L0,680 Z"/>
      <path fill="var(--paper)" d="M0,0 C110,44 220,50 326,54 C332,55 334,60 334,68 C336,250 316,430 176,598 C128,648 62,674 20,680 L0,680 Z"/>
    </svg>

    <div class="brand-name">Bastion Crest</div>

    <h1 class="holder-name">Marcus Delvane</h1>

    <address class="contact">
      P.O. Box 7352<br>
      Ferndale nsw 2291<br>
      T: 0437682915<br>
      E:marcus@bastioncrest.com.au
    </address>

    <h2 class="company-name">Bastion Crest Security Group</h2>

    <p class="registration">Abn-47318265094 Acn-318265094</p>
  </section>
</body>
</html>
```